Commercial wall and ceiling contractor needs website

Construction trade companies are notoriously behind the rest of the world when it comes to using current technology to run their businesses; we are not one of those companies. We are a walls and ceilings contractor using up to date communications technologies and applying them unlike any other in our trade. As simple as it sounds, and it really is that simple, it is still a new idea in the trade. We are moving our customers towards communicating with us through a single point of contact using text and email; we distribute information to the appropriate internal party on our end. We need a website that generally appears traditionally familiar to the visitor while also expresses a fresh new approach and edginess to the trade business.

Target Market(s)

General contractors looking to get a bit of background info before inviting us to bid on their projects. This is not a high traffic environment. Their subsequent site visits will be primarily for contact info.

Industry/Entity Type

Construction Company

Number of Pages Required

3 page

Font styles to use
Sans Serif

Requirements
Must have
• The file I uploaded named "kolsite.docx" does not have to appear on the site in the same manner in which appears in the document file; but the info contained within that document does need to be represented on the site.

```html
<!DOCTYPE html>
<html lang="en">
<head>
<meta charset="utf-8">
<title>Stratline Walls and Ceilings</title>
<link href="https://fonts.googleapis.com/css2?family=Montserrat:wght@500;600;700;800&family=Lato:ital,wght@0,400;0,700;1,400&display=swap" rel="stylesheet">
<style>
:root{
  --gold:#b8892f;
  --green:#176b4a;
  --ink:#1f1f1f;
  --text:#6b6b6b;
  --white:#ffffff;
  --chart-blue:#3f86c4;
  --chart-teal:#2f9e82;
}
*{box-sizing:border-box;margin:0;padding:0}
html,body{width:1200px;height:4615px;overflow:hidden}
body{position:relative;background:var(--white);font-family:"Lato",Arial,sans-serif;color:var(--text)}
.abs{position:absolute}
.topbar{left:0;top:0;width:1200px;height:45px;background:var(--gold);color:var(--white);font-size:12px}
.topbar .mail{left:165px;top:15px;display:flex;gap:10px;align-items:center}
.topbar .phone{right:134px;top:15px;display:flex;gap:10px;align-items:center}
.nav{left:0;top:45px;width:1200px;height:77px;background:var(--white)}
.brand{left:165px;top:22px;display:flex;align-items:center;gap:10px;font-family:"Montserrat",sans-serif;font-weight:700;font-size:20px;color:var(--green);letter-spacing:.04em}
.brand .mark{width:24px;height:24px;border:4px solid var(--green)}
.menu{right:134px;top:32px;display:flex;gap:34px;font-size:13px;color:var(--ink)}
.menu .active{color:var(--green);position:relative}
.menu .active::after{content:"";position:absolute;left:-3px;right:-3px;bottom:-12px;height:2px;background:var(--green)}
.hero{left:0;top:122px;width:1200px;height:654px;border-radius:0 0 70px 70px;overflow:hidden}
.hero-photo{left:0;top:0;width:1200px;height:654px;background:linear-gradient(120deg,#4a4540 0%,#2c2a28 50%,#3a3733 100%)}
.hero-title{right:138px;top:175px;text-align:right;font-family:"Montserrat",sans-serif;font-weight:800;font-size:66px;line-height:78px;color:var(--gold)}
.hero-copy{right:138px;top:338px;width:470px;text-align:right;color:var(--white);font-size:16.5px;line-height:24px}
.btn{display:inline-block;background:var(--gold);color:var(--white);font-family:"Montserrat",sans-serif;font-weight:700;letter-spacing:.04em;border-radius:7px 0 7px 0}
.hero .btn{position:absolute;right:134px;top:438px;width:154px;height:51px;line-height:51px;text-align:center;font-size:16px}
.slides{left:1140px;top:228px;width:20px;color:var(--white);font-size:13px;text-align:center}
.slides span{display:block}
.slides .cur{color:var(--gold);font-size:17px;font-weight:700}
.heading{display:flex;align-items:center;height:60px}
.heading.center{left:0;width:1200px;justify-content:center}
.heading .bar{width:6px;height:52px;background:var(--gold);margin-right:18px;flex:none}
.heading h2{font-family:"Montserrat",sans-serif;font-weight:600;font-size:38px;letter-spacing:.32em;color:var(--ink)}
.copy{font-size:12.5px;line-height:23px;color:var(--text)}
.copy p+p{margin-top:22px}
.small-btn{height:38px;line-height:38px;padding:0 16px;font-size:13px}
.photo{background:linear-gradient(135deg,#c9c2b8,#9c948a)}
.chart{border-radius:50%;background:conic-gradient(var(--chart-teal) 0 25%,var(--chart-blue) 25% 50%,#6cc0e6 50% 75%,#1c8f6c 75% 100%)}
.card{background:var(--white);box-shadow:0 1px 6px rgba(0,0,0,.18)}
.card h3{font-family:"Montserrat",sans-serif;font-weight:700;color:var(--ink)}
.service h3{font-size:17px;margin:24px 14px 8px}
.service p{margin:0 14px;font-size:12px;line-height:23px}
.service .btn{margin:16px 14px 0;font-size:13px;height:37px;line-height:37px;padding:0 15px}
.news h3{font-size:13px;margin:18px 14px 4px;white-space:nowrap}
.news .date{margin:0 14px;color:var(--gold);font-size:9px}
.news p{margin:6px 14px 0;font-size:11px;line-height:20px}
.testimonial{left:308px;top:3224px;width:614px;height:250px;border:1px solid #ddd;border-radius:4px;box-shadow:0 2px 8px rgba(0,0,0,.12);background:var(--white);text-align:center}
.stack{border:1px solid #e3e3e3;background:var(--white);border-top:none;border-radius:0 0 4px 4px}
.testimonial .name{margin-top:68px;font-family:"Montserrat",sans-serif;font-weight:700;font-size:11px;color:var(--ink)}
.testimonial .quote{margin:14px 28px 0;font-style:italic;font-size:11px;line-height:20px}
.dots{display:flex;justify-content:center;gap:18px;margin-top:26px}
.dots span{width:9px;height:9px;transform:rotate(45deg);border:1px solid var(--gold)}
.dots .on{background:var(--green);border-color:var(--green)}
.field{height:36px;border:1px solid #ccc;border-radius:2px;font-size:11px;padding:11px 12px;color:var(--text)}
.contact-box{height:115px;color:var(--white);border-radius:0 0 22px 0}
.contact-box h4{font-family:"Montserrat",sans-serif;font-weight:600;font-size:17px}
.contact-box p{font-size:11.5px;margin-top:6px}
.contact-box .note{font-size:9.5px;text-transform:uppercase;margin-top:9px}
.footer-links{left:165px;top:4514px;display:flex;gap:34px;font-size:12px;color:var(--ink)}
.socials{left:917px;top:4508px;display:flex;gap:10px}
.socials span{width:31px;height:31px;border-radius:50%;border:2px solid var(--gold)}
.copyright{left:0;top:4581px;width:1200px;text-align:center;font-size:10.5px;color:var(--ink)}
</style>
</head>
<body>

<header>
  <div class="abs topbar">
    <div class="abs mail">
      <svg width="18" height="13" viewBox="0 0 18 13"><rect x="1" y="1" width="16" height="11" fill="none" stroke="#fff" stroke-width="1.5"/><path d="M1 1l8 6 8-6" fill="none" stroke="#fff" stroke-width="1.5"/></svg>
      <span>hello@stratlinewalls.com</span>
    </div>
    <div class="abs phone">
      <svg width="16" height="16" viewBox="0 0 24 24"><path d="M6.6 10.8a15 15 0 006.6 6.6l2.2-2.2a1 1 0 011-.25 11 11 0 003.6.6 1 1 0 011 1V20a1 1 0 01-1 1A17 17 0 013 4a1 1 0 011-1h3.5a1 1 0 011 1 11 11 0 00.6 3.6 1 1 0 01-.25 1z" fill="#fff"/></svg>
      <span>604-555-0182</span>
    </div>
  </div>
  <nav class="abs nav">
    <div class="abs brand"><span class="mark"></span>STRATLINE</div>
    <div class="abs menu">
      <span class="active">Home</span><span>About Us</span><span>Services</span><span>Testimonials</span><span>News</span><span>Contact Us</span>
    </div>
  </nav>
</header>

<section class="abs hero">
  <div class="abs hero-photo" role="img" aria-label="Tradesman in a hard hat installing a ceiling board, seen through framed panels"></div>
  <h1 class="abs hero-title">STRATLINE WALLS<br>AND CEILINGS</h1>
  <p class="abs hero-copy">We are a walls and ceilings contractor using up to date communications technologies and applying them unlike any other in our trade.</p>
  <span class="btn">CONTACT US</span>
  <div class="abs slides">
    <span>01</span><span style="margin-top:14px">02</span>
    <svg width="20" height="70" viewBox="0 0 20 70"><line x1="10" y1="8" x2="10" y2="62" stroke="#b8892f" stroke-width="1.5"/><path d="M6 58l4 5 4-5" fill="none" stroke="#b8892f" stroke-width="1.5"/></svg>
    <span class="cur">03</span><span style="margin-top:10px">04</span>
  </div>
</section>

<section class="about">
  <div class="abs heading" style="left:165px;top:896px">
    <span class="bar"></span><h2>ABOUT US</h2>
  </div>
  <div class="abs copy" style="left:165px;top:1018px;width:438px">
    <p>Lorem Ipsum is simply dummy text of the printing and typesetting industry. Lorem Ipsum has been the industry's standard dummy text ever since the 1500s, when an unknown printer took a galley of type and scrambled it to make a type specimen book.</p>
    <p>It was popularised in the 1960s with the release of transfer sheets containing Lorem Ipsum passages, and more recently with desktop publishing software including versions of Lorem Ipsum.</p>
  </div>
  <span class="abs btn small-btn" style="left:165px;top:1237px">READ MORE</span>
  <div class="abs photo" style="left:627px;top:890px;width:560px;height:342px;background:linear-gradient(120deg,#d8cfc2,#b7aa98 55%,#8f8478)" role="img" aria-label="Smiling plasterer in red overalls holding a trowel beside a stepladder"></div>
</section>

<section class="why">
  <div class="abs heading center" style="top:1376px">
    <span class="bar"></span><h2>WHY US?</h2>
  </div>
  <div class="abs copy" style="left:330px;top:1484px;width:570px;text-align:center;font-size:11.5px;line-height:20px">
    <p>Today's communication landscape is dramatically different than it was a mere ten years ago. We use our phones less and less for making calls. In fact, it is reported that 70% of direct communication is through text messaging, not phone calls; with text messaging increasing in use by %7,700 since 2008. No surprise here.</p>
    <p>Think of the phone call process; auto attendant, "…choose 1 for…", "…if you know the extension…", "…spell the name…", "…to hear a directory…", etc.; ugh. I don't know about you but when I finally get to the person I want to speak with, I often forget why I called in the first place. And let's not get started on voicemail; I mean really, who likes leaving a voice message let alone retrieving one.</p>
  </div>

  <div class="abs chart" style="left:317px;top:1748px;width:150px;height:150px" role="img" aria-label="Infographic on how many adults, clients and businesses prefer texting"></div>
  <div class="abs copy" style="left:627px;top:1750px;width:440px;font-size:11.5px;line-height:23px">
    <p>One of the many ways that Stratline is bringing technology to its trade is through communication tools. A single point of contact gets you where you want to go. We distribute the text and email internally.</p>
    <p>Not only that, we share equal access to our communication points to hold each other accountable for their respective responsibilities. This flow of information is a more efficient, effective, and direct.</p>
  </div>

  <div class="abs copy" style="left:165px;top:2035px;width:430px;font-size:11.5px;line-height:23px">
    <p>The average length of a phone call has sharply decreased since 2006. That's because it's easier to swap a bunch of short messages than it is to interrupt each other's work at hand with a phone call.</p>
    <p>Furthermore, 99% of text messages are read while only 33% of voicemail messages are heard; 95% of text messages are read within 3 minutes and, on average, responded to within 90 seconds.</p>
  </div>
  <div class="abs chart" style="left:758px;top:2047px;width:132px;height:132px" role="img" aria-label="Infographic on text reading and reply times"></div>
</section>

<section class="services">
  <div class="abs heading center" style="top:2347px">
    <span class="bar"></span><h2>OUR SERVICE</h2>
  </div>
  <article class="abs card service" style="left:165px;top:2498px;width:440px;height:479px">
    <div class="photo" style="height:269px;background:linear-gradient(135deg,#a9a7a4,#d6d3cf 60%,#8c8a87)" role="img" aria-label="Worker in a hard hat plastering a wall above a stairway"></div>
    <h3>Walls Contracting</h3>
    <p>Lorem Ipsum is simply dummy text of the printing and typesetting industry. Lorem Ipsum has been the industry's standard dummy text ever since the 1500s, when an unknown printer took a galley of type and scrambled it to make a type specimen book.</p>
    <span class="btn">READ MORE</span>
  </article>
  <article class="abs card service" style="left:627px;top:2498px;width:440px;height:479px">
    <div class="photo" style="height:269px;background:linear-gradient(135deg,#8f8c88,#c9c6c1 55%,#7a7773)" role="img" aria-label="Worker drilling into a ceiling grid"></div>
    <h3>Ceilings Contracting</h3>
    <p>Lorem Ipsum is simply dummy text of the printing and typesetting industry. Lorem Ipsum has been the industry's standard dummy text ever since the 1500s, when an unknown printer took a galley of type and scrambled it to make a type specimen book.</p>
    <span class="btn">READ MORE</span>
  </article>
</section>

<section class="testimonials">
  <div class="abs heading center" style="top:3063px">
    <span class="bar"></span><h2>OUR TESTIMONIALS</h2>
  </div>
  <div class="abs stack" style="left:328px;top:3475px;width:574px;height:12px"></div>
  <div class="abs stack" style="left:346px;top:3487px;width:538px;height:10px"></div>
  <div class="abs testimonial">
    <p class="name">-CLIENT NAME</p>
    <p class="quote">" Lorem Ipsum is simply dummy text of the printing and typesetting industry. Lorem Ipsum has been the industry's standard dummy text ever since the 1500s, when an unknown printer took a galley of type and scrambled it to make a type specimen book.</p>
    <p class="quote" style="margin-top:18px">It has survived not only five centuries, but also the leap into electronic typesetting, remaining essentially unchanged. "</p>
    <div class="dots"><span></span><span class="on"></span><span></span></div>
  </div>
  <div class="abs photo" style="left:573px;top:3170px;width:84px;height:99px;background:linear-gradient(160deg,#9aa6ad,#3d4a55)" role="img" aria-label="Client portrait in a dark suit"></div>
  <svg class="abs" style="left:335px;top:3206px" width="46" height="46" viewBox="0 0 46 46"><circle cx="23" cy="23" r="22" fill="#b8892f"/><path d="M13 28q0-9 7-12v3q-3 2-3 5h3v6h-7zM25 28q0-9 7-12v3q-3 2-3 5h3v6h-7z" fill="#fff"/></svg>
</section>

<section class="news-list">
  <div class="abs heading center" style="top:3570px">
    <span class="bar"></span><h2>LATEST NEWS</h2>
  </div>
  <article class="abs card news" style="left:165px;top:3711px;width:286px;height:349px">
    <div class="photo" style="height:193px;background:linear-gradient(135deg,#d9d6d1,#a8a39c)" role="img" aria-label="Plasterer crouching beside buckets in a white room"></div>
    <h3>Lorem Ipsum is simply dummy text.</h3>
    <p class="date">July 17, 2018</p>
    <p>Lorem Ipsum is simply dummy text of the printing and typesetting industry. Lorem Ipsum has been the industry's standard dummy text ever since the 1500s.</p>
  </article>
  <article class="abs card news" style="left:471px;top:3711px;width:287px;height:349px">
    <div class="photo" style="height:193px;background:linear-gradient(135deg,#c7bca9,#efeae2 60%,#5a5550)" role="img" aria-label="Worker holding a white hard hat beside a ladder"></div>
    <h3>Lorem Ipsum is simply dummy text.</h3>
    <p class="date">April 23, 2018</p>
    <p>Lorem Ipsum is simply dummy text of the printing and typesetting industry. Lorem Ipsum has been the industry's standard dummy text ever since the 1500s.</p>
  </article>
  <article class="abs card news" style="left:779px;top:3711px;width:287px;height:349px">
    <div class="photo" style="height:193px;background:linear-gradient(135deg,#e4e2df,#b9b5b0 60%,#9e4a3f)" role="img" aria-label="Worker in a red shirt fixing a ceiling panel"></div>
    <h3>Lorem Ipsum is simply dummy text.</h3>
    <p class="date">March 21, 2018</p>
    <p>Lorem Ipsum is simply dummy text of the printing and typesetting industry. Lorem Ipsum has been the industry's standard dummy text ever since the 1500s.</p>
  </article>
</section>

<section class="newsletter">
  <div class="abs heading center" style="top:4134px">
    <span class="bar"></span><h2>NEWSLETTER</h2>
  </div>
  <p class="abs" style="left:0;top:4234px;width:1200px;text-align:center;font-size:11.5px">Subscribe us and get latest news, updates and offers in your inbox.</p>
  <div class="abs field" style="left:272px;top:4280px;width:269px">Enter Name:</div>
  <div class="abs field" style="left:559px;top:4280px;width:268px">Enter Email:</div>
  <span class="abs btn" style="left:849px;top:4280px;width:107px;height:36px;line-height:36px;text-align:center;font-size:11px">SUBSCRIBE!</span>
</section>

<footer>
  <div class="abs contact-box" style="left:165px;top:4366px;width:439px;background:var(--gold)">
    <svg class="abs" style="left:24px;top:48px" width="20" height="20" viewBox="0 0 24 24"><path d="M6.6 10.8a15 15 0 006.6 6.6l2.2-2.2a1 1 0 011-.25 11 11 0 003.6.6 1 1 0 011 1V20a1 1 0 01-1 1A17 17 0 013 4a1 1 0 011-1h3.5a1 1 0 011 1 11 11 0 00.6 3.6 1 1 0 01-.25 1z" fill="#fff"/></svg>
    <div class="abs" style="left:70px;top:16px"><h4>Contact</h4><p>604-555-0182</p><p class="note">If you have any contact us now.</p></div>
    <svg class="abs" style="left:360px;top:52px;opacity:.25" width="56" height="56" viewBox="0 0 24 24"><path d="M6.6 10.8a15 15 0 006.6 6.6l2.2-2.2a1 1 0 011-.25 11 11 0 003.6.6 1 1 0 011 1V20a1 1 0 01-1 1A17 17 0 013 4a1 1 0 011-1h3.5a1 1 0 011 1 11 11 0 00.6 3.6 1 1 0 01-.25 1z" fill="#fff"/></svg>
  </div>
  <div class="abs contact-box" style="left:627px;top:4366px;width:439px;background:var(--green)">
    <svg class="abs" style="left:24px;top:50px" width="22" height="16" viewBox="0 0 18 13"><rect x="1" y="1" width="16" height="11" fill="none" stroke="#fff" stroke-width="1.5"/><path d="M1 1l8 6 8-6" fill="none" stroke="#fff" stroke-width="1.5"/></svg>
    <div class="abs" style="left:70px;top:16px"><h4>Email Address</h4><p>office@stratlinewalls.com</p><p class="note">Email us now for more informations.</p></div>
    <svg class="abs" style="left:360px;top:58px;opacity:.25" width="66" height="46" viewBox="0 0 18 13"><rect x="1" y="1" width="16" height="11" fill="none" stroke="#fff" stroke-width="1.2"/><path d="M1 1l8 6 8-6" fill="none" stroke="#fff" stroke-width="1.2"/></svg>
  </div>
  <nav class="abs footer-links"><span>Home</span><span>About Us</span><span>Services</span><span>Testimonials</span><span>News</span><span>Contact Us</span></nav>
  <div class="abs socials" aria-label="Social media links"><span></span><span></span><span></span><span></span></div>
  <p class="abs copyright">Copyright © 2019 <strong>Stratline Walls and Ceiling Contractor.</strong> All Rights Reserved. Terms &amp; Conditions | Privacy Policy.</p>
</footer>

</body>
</html>
```